Design the Keystone HR business card for my new business

I've just had a logo designed (attached) for my new business doing HR consulting. I'm a one person operation at this stage, my aim is to provide support and help to small to medium sized businesses with their people objectives or issues.

I'm not really into anything overly flashy, I'm not a PR or marketing agency. I'd like my card to look modern, professional and not gimmicky.

I'm thinking black front (to go with logo), double sided with details on the back, maybe in a different colour?

Logo attached in several different formats.

Front of the card to have logo and added text: Practical People and Team Support

Back of the card to also feature logo in some way and say:
Megan Tulloch
PO Box (TBA)
Marrowvale QLD 4391
0438 512 976
megan@keystonehr.com.au
www.keystonehr.com.au

Target Market(s)

Small to medium businesses / business owners.

Industry/Entity Type

Marketing

Requirements
Must have
• Double sided business card.
Should not have
• Anything overly gimmicky.

```html
<!DOCTYPE html>
<html lang="en">
<head>
<meta charset="utf-8">
<title>Keystone HR Consulting – Business Card</title>
<link rel="stylesheet" href="https://fonts.googleapis.com/css2?family=Montserrat:wght@300&family=PT+Sans:ital,wght@0,400;0,700;1,400&display=swap">
<style>
  :root {
    --page: #ffffff;
    --card: #000000;
    --ink: #ffffff;
    --accent: #a23fd0;
    --accent-line: #8e2fc4;
  }
  * { box-sizing: border-box; margin: 0; padding: 0; }
  html, body {
    width: 1007px;
    height: 1200px;
    overflow: hidden;
    background: var(--page);
  }
  .sheet { position: relative; width: 1007px; height: 1200px; }
  .card {
    position: absolute;
    left: 50px;
    width: 925px;
    background: var(--card);
    color: var(--ink);
    overflow: hidden;
  }
  .card--front { top: 66px; height: 528px; }
  .card--back  { top: 658px; height: 530px; }

  .brand-mark { position: absolute; display: block; }
  .brand-name {
    position: absolute;
    font-family: "Montserrat", sans-serif;
    font-weight: 300;
    color: var(--ink);
    white-space: nowrap;
    letter-spacing: 0.3px;
    line-height: 1;
  }

  .card--front .brand-mark { left: 105px; top: 54px; width: 233px; height: 233px; }
  .card--front .brand-name { left: 62px; top: 352px; font-size: 44px; }
  .tagline {
    position: absolute;
    left: 128px;
    top: 440px;
    font-family: "PT Sans", sans-serif;
    font-style: italic;
    font-size: 30px;
    line-height: 36px;
    color: var(--accent);
    white-space: nowrap;
  }

  .card--back .brand-mark { left: 47px; top: 44px; width: 148px; height: 148px; }
  .card--back .brand-name { left: 51px; top: 212px; font-size: 23px; }

  .contact {
    position: absolute;
    right: 55px;
    top: 158px;
    text-align: right;
    font-family: "PT Sans", sans-serif;
  }
  .contact__name {
    font-weight: 700;
    font-size: 38px;
    line-height: 44px;
    text-transform: lowercase;
  }
  .contact__role {
    font-size: 31px;
    line-height: 42px;
    color: var(--accent);
    text-transform: lowercase;
  }
  .contact__details {
    margin-top: 44px;
    font-style: normal;
    font-size: 25px;
    line-height: 37px;
  }
  .contact__web { color: var(--accent); }
</style>
</head>
<body>
<main class="sheet">
  <section class="card card--front" aria-label="Card front">
    <svg class="brand-mark" viewBox="0 0 100 100" aria-hidden="true">
      <circle cx="50" cy="50" r="48" fill="none" stroke="var(--accent-line)" stroke-width="1.2"/>
    </svg>
    <p class="brand-name">Keystone HR Consulting</p>
    <p class="tagline">Practical People and Team Support</p>
  </section>

  <section class="card card--back" aria-label="Card back">
    <svg class="brand-mark" viewBox="0 0 100 100" aria-hidden="true">
      <circle cx="50" cy="50" r="48" fill="none" stroke="var(--accent-line)" stroke-width="1.6"/>
    </svg>
    <p class="brand-name">Keystone HR Consulting</p>

    <div class="contact">
      <h1 class="contact__name">Megan Tulloch</h1>
      <p class="contact__role">Consultant</p>
      <address class="contact__details">
        PO Box (TBA)<br>
        Marrowvale QLD 4391<br>
        0438 512 976<br>
        megan@keystonehr.com.au<br>
        <span class="contact__web">www.keystonehr.com.au</span>
      </address>
    </div>
  </section>
</main>
</body>
</html>
```